Accounting business needs a great flyer

I need a flyer for my new business "Bright Ledger". I am an individual accountant working for himself on the Sunshine Coast in Queensland Australia. I would like to see designs that communicate reliability and trust. I believe my point of difference is that I am always available to my clients and I will cap my number of clients to ensure I can service them properly.
The main point I want to convey is that most of the time junior employees with little to no experience or unqualified employees do the tax work for the clients and a senior accountant quickly checks the work at the end but never gets to really know the clients business. Accountants in general seem to have a bad reputation for not responding to clients in a timely fashion, whether by email or phone. This is where I intend to differentiate myself. . I have also included some logo's that should go on the flyer.

Target Market(s)

Every small business

Industry/Entity Type

Public Accounting

Requirements
Must have
• Web address: www.brightledger.com.au
Phone number: 0418 592 637
Attached logos
Reference to: "Do you know who is actually doing your tax?"
Other accounting firms - use junior unqualified staff
- outsource to cheap labour countries
- use tax consultants who sometimes have had only 2 weeks training.
At Bright Ledger, a highly qualified plain badge shape with a Masters in Taxation does your work from start to finish.
**I don't need it to say exactly this but I want the theme of the flyer to have these points in it.
Nice to have
• Something different

```html
<!DOCTYPE html>
<html lang="en">
<head>
<meta charset="utf-8">
<title>Bright Ledger – Individual &amp; Small Business Accounting</title>
<link rel="stylesheet" href="https://fonts.googleapis.com/css2?family=Raleway:wght@500;600&family=Montserrat:wght@600;700;800&family=Oswald:wght@500;600;700&display=swap">
<style>
  :root{
    --backdrop:#d2d2d4;
    --navy:#25246b;
    --navy-deep:#1d1c58;
    --royal:#3a3f9c;
    --gold:#f5b800;
    --white:#ffffff;
    --ink:#1d1c58;
    --lemon:#f6ef2a;
    --badge:rgba(255,255,255,.16);
  }
  *{box-sizing:border-box;margin:0;padding:0}
  html,body{width:1200px;height:1000px;overflow:hidden;background:var(--backdrop)}
  .flyer{position:absolute;left:278px;top:42px;width:642px;height:906px;overflow:hidden;background:var(--navy)}
  .flyer-shapes{position:absolute;inset:0}
  .brand{position:absolute;left:330px;top:140px;width:310px;text-align:center}
  .brand-mark{display:block;width:88px;height:88px;margin:0 auto 16px;border:3px solid var(--white);border-radius:50%}
  .brand-name{font-family:"Raleway",sans-serif;font-weight:600;font-size:22px;letter-spacing:4px;color:var(--gold);white-space:nowrap}
  .headline{position:absolute;left:322px;top:306px;width:330px;text-align:center;font-family:"Raleway",sans-serif;font-weight:500;font-size:45px;line-height:43px;color:var(--white)}
  .services-tag{position:absolute;left:38px;top:461px;width:254px;height:45px;background:var(--gold);border-radius:0 14px 14px 0;font-family:"Montserrat",sans-serif;font-weight:800;font-size:26px;line-height:45px;color:var(--ink);padding-left:10px;white-space:nowrap}
  .services{position:absolute;left:36px;top:532px;width:260px;list-style:none;font-family:"Montserrat",sans-serif;font-weight:700;font-size:14px;line-height:16px;color:var(--white)}
  .services li{position:absolute;left:0;display:flex;gap:14px;align-items:flex-start;width:260px}
  .tick{flex:0 0 20px;width:20px;height:20px;margin-top:-2px}
  .accreditations{position:absolute;left:38px;top:785px;display:flex;align-items:center;gap:20px}
  .badge{width:60px;height:60px;border-radius:10px;background:var(--badge)}
  .contact-bar{position:absolute;left:0;top:860px;width:642px;height:46px}
  .contact{position:absolute;top:860px;height:46px;display:flex;align-items:center;gap:8px;font-family:"Oswald",sans-serif;font-weight:600;color:var(--ink);white-space:nowrap}
  .contact svg{width:18px;height:18px}
  .contact-phone{left:34px;font-size:22px}
  .contact-web{left:208px;font-size:21px}
  .contact-divider{position:absolute;left:193px;top:866px;width:2px;height:34px;background:var(--ink)}
  .question{position:absolute;right:32px;top:614px;text-align:right;font-family:"Oswald",sans-serif;font-weight:700;font-size:28px;line-height:34px;color:var(--white);letter-spacing:.3px;white-space:nowrap}
  .claim{position:absolute;right:50px;top:688px;text-align:right;font-family:"Montserrat",sans-serif;font-weight:700;font-size:12.5px;line-height:18px;color:var(--white);white-space:nowrap}
  .claim-dot{position:absolute;right:34px;top:694px;width:8px;height:8px;border-radius:50%;background:#e6e021}
  .rule{position:absolute;right:32px;top:786px;width:110px;height:3px;background:var(--white)}
  .promise-lead{position:absolute;right:32px;top:798px;font-family:"Montserrat",sans-serif;font-weight:800;font-size:23px;color:var(--lemon);white-space:nowrap}
  .promise{position:absolute;right:32px;top:832px;text-align:right;font-family:"Montserrat",sans-serif;font-weight:700;font-size:12.5px;line-height:17px;color:var(--white);white-space:nowrap}
</style>
</head>
<body>
<main class="flyer">
  <svg class="flyer-shapes" viewBox="0 0 642 906" width="642" height="906">
    <defs>
      <linearGradient id="city-tone" x1="0" y1="0" x2="1" y2="1">
        <stop offset="0" stop-color="#cfe6f6"/>
        <stop offset=".45" stop-color="#7fb3e0"/>
        <stop offset="1" stop-color="#3e5fb5"/>
      </linearGradient>
      <linearGradient id="desk-tone" x1="0" y1="0" x2="1" y2="1">
        <stop offset="0" stop-color="#e3b21c"/>
        <stop offset="1" stop-color="#b98d10"/>
      </linearGradient>
    </defs>
    <polygon points="0,0 642,0 642,300 230,460 0,340" fill="url(#city-tone)" role="img" aria-label="Photo of business people walking through a bright city office"/>
    <polygon points="0,340 230,460 0,560" fill="var(--navy-deep)"/>
    <polygon points="642,440 642,906 412,906 232,658 360,540" fill="url(#desk-tone)" role="img" aria-label="Photo of a hand writing on paperwork at a desk, tinted gold"/>
    <polygon points="560,120 642,120 642,320" fill="var(--navy-deep)" opacity=".7"/>
    <g transform="translate(470 370) rotate(45)">
      <rect x="-188" y="-188" width="376" height="376" rx="26" fill="var(--royal)" stroke="var(--gold)" stroke-width="4"/>
    </g>
    <polygon points="0,860 440,860 476,906 0,906" fill="var(--gold)"/>
  </svg>

  <div class="brand">
    <span class="brand-mark"></span>
    <span class="brand-name">BRIGHT LEDGER</span>
  </div>

  <h1 class="headline">Individual &amp;<br>Small<br>Business<br>Accounting</h1>

  <h2 class="services-tag">OUR SERVICES</h2>
  <ul class="services">
    <li style="top:0"><svg class="tick" viewBox="0 0 20 20"><circle cx="10" cy="10" r="10" fill="#f5b800"/><path d="M5 10.5l3.2 3.2L15 6.8" fill="none" stroke="#fff" stroke-width="2.4"/></svg>Tax Return Preparation</li>
    <li style="top:28px"><svg class="tick" viewBox="0 0 20 20"><circle cx="10" cy="10" r="10" fill="#f5b800"/><path d="M5 10.5l3.2 3.2L15 6.8" fill="none" stroke="#fff" stroke-width="2.4"/></svg>Company &amp; Trust Returns &amp;<br>Financials</li>
    <li style="top:72px"><svg class="tick" viewBox="0 0 20 20"><circle cx="10" cy="10" r="10" fill="#f5b800"/><path d="M5 10.5l3.2 3.2L15 6.8" fill="none" stroke="#fff" stroke-width="2.4"/></svg>Rental Property Returns</li>
    <li style="top:100px"><svg class="tick" viewBox="0 0 20 20"><circle cx="10" cy="10" r="10" fill="#f5b800"/><path d="M5 10.5l3.2 3.2L15 6.8" fill="none" stroke="#fff" stroke-width="2.4"/></svg>BLRC Reporting</li>
    <li style="top:128px"><svg class="tick" viewBox="0 0 20 20"><circle cx="10" cy="10" r="10" fill="#f5b800"/><path d="M5 10.5l3.2 3.2L15 6.8" fill="none" stroke="#fff" stroke-width="2.4"/></svg>Advice</li>
    <li style="top:152px"><svg class="tick" viewBox="0 0 20 20"><circle cx="10" cy="10" r="10" fill="#f5b800"/><path d="M5 10.5l3.2 3.2L15 6.8" fill="none" stroke="#fff" stroke-width="2.4"/></svg>Tax Planning</li>
    <li style="top:180px"><svg class="tick" viewBox="0 0 20 20"><circle cx="10" cy="10" r="10" fill="#f5b800"/><path d="M5 10.5l3.2 3.2L15 6.8" fill="none" stroke="#fff" stroke-width="2.4"/></svg>BAS / IAS Preparation &amp;<br>Lodgements</li>
    <li style="top:224px"><svg class="tick" viewBox="0 0 20 20"><circle cx="10" cy="10" r="10" fill="#f5b800"/><path d="M5 10.5l3.2 3.2L15 6.8" fill="none" stroke="#fff" stroke-width="2.4"/></svg>Company &amp; Trust Set ups</li>
  </ul>

  <div class="accreditations" aria-label="Professional accreditations">
    <span class="badge"></span>
    <span class="badge"></span>
    <span class="badge"></span>
  </div>

  <div class="contact contact-phone">
    <svg viewBox="0 0 18 18"><circle cx="9" cy="9" r="9" fill="#1d1c58"/><path d="M6 4.5l1.6 2.4-1 1.1c.6 1.3 1.5 2.2 2.8 2.8l1.1-1 2.4 1.6-.8 1.6c-3.4.2-7.1-3.5-6.9-6.9z" fill="#f5b800"/></svg>
    0418 592 637
  </div>
  <span class="contact-divider"></span>
  <div class="contact contact-web">
    <svg viewBox="0 0 18 18"><circle cx="9" cy="9" r="9" fill="#1d1c58"/><circle cx="9" cy="9" r="4.5" fill="none" stroke="#f5b800" stroke-width="1.4"/><path d="M4.5 9h9M9 4.5c-2 2.6-2 6.4 0 9M9 4.5c2 2.6 2 6.4 0 9" fill="none" stroke="#f5b800" stroke-width="1"/></svg>
    brightledger.com.au
  </div>

  <h3 class="question">DO YOU KNOW WHO IS<br>ACTUALLY DOING YOUR TAX?</h3>
  <span class="claim-dot"></span>
  <p class="claim">It is common practice in many accounting<br>firms to use unqualified staff, junior staff or<br>even send your work offshore to cheap labour<br>countries to do the processing.</p>
  <span class="rule"></span>
  <p class="promise-lead">At Bright Ledger,</p>
  <p class="promise">a highly qualified CPA with a<br>Masters in Taxation does your<br>work from start to finish.</p>
</main>
</body>
</html>
```